Buch-/eBook-Cover für Traumatherapeutin
Zielgruppe
Ich bin Traumatherapeutin und schreibe ein Buch zum Thema Trauma bearbeiten.
Meine Zielgruppe sucht Heilung, Genesung, Selbstliebe etc.
Aufgabenstellung
Buchcover
Bitte erstell mir ein modernes positives inspirierendes Buchcover mit dem
Titel: 'Morgens LEISE aufbrechen“
Untertitel: „Geh den Pfad, der dich leise ruft“
Dr. Merle Kuhnast
Ich hätte gerne ein modernes Buch, das entweder einen Bezug zum Thema Trauma hat oder aber einfach stylische Schriftzüge. Bin aber auch offen für andere Vorschläge.
Dunkelblau, weiß und türkis oder auch rosa mag ich ganz gerne. Wobei Dunkelblau, weiß und türkis meine Favoriten sind und mit rosa höchstens kleinere Akzente gesetzt werden sollten.
Das Buchcover soll modern sein und direkt ansprechen. Gerne eine originelle Lösung, oder etwas Besonderes, etwas das Tiefe ausdrückt, oder man mehrmals hinsehen muss um etwas zu erkennen oder etwas das mehr Interpretationsspielraum lässt.
Gerne auch viel weiß, zumindest heller und nicht zu dunkel. Stylish, aber nicht überfrachtet.
Schreib mich gerne an, wenn du Fragen hast.
Ich habe mal zwei Beispiel von Typolösungen angehängt, die ich ganz cool fände.
Ich freue mich auf deine Ideen :-)
Ganz liebe Grüße
Merle

```html
<!DOCTYPE html>
<html lang="de">
<head>
<meta charset="utf-8">
<title>Morgens leise aufbrechen – Buchcover</title>
<link rel="stylesheet" href="https://fonts.googleapis.com/css2?family=Source+Sans+3:wght@400;500&family=Dancing+Script:wght@700&family=Yellowtail&display=swap">
<style>
  :root {
    --stage: #575757;
    --paper: #ffffff;
    --title-blue: #4b79a1;
    --script-blue: #3c5d8d;
    --wash-deep: #7fb6dc;
    --wash-mid: #a9d3ee;
    --wash-light: #dcedf9;
    --swoosh: #c6e0f2;
  }
  * { margin: 0; padding: 0; box-sizing: border-box; }
  html, body { width: 908px; height: 1200px; overflow: hidden; }
  body { background: var(--stage); position: relative; }

  .cover {
    position: absolute;
    left: 70px; top: 56px;
    width: 768px; height: 1086px;
    background: var(--paper);
    overflow: hidden;
  }

  .cover__author {
    position: absolute; left: 0; right: 0; top: 92px;
    text-align: center;
    font-family: "Source Sans 3", sans-serif;
    font-weight: 500;
    font-size: 40px;
    letter-spacing: 1px;
    color: var(--title-blue);
  }

  .cover__wash {
    position: absolute;
    left: -10px; top: 200px;
    width: 790px; height: 540px;
    border-radius: 46% 40% 48% 38% / 48% 44% 52% 46%;
    background:
      radial-gradient(ellipse 30% 45% at 22% 42%, var(--wash-deep) 0%, transparent 70%),
      radial-gradient(ellipse 35% 40% at 78% 60%, var(--wash-mid) 0%, transparent 75%),
      radial-gradient(ellipse 55% 50% at 50% 50%, var(--wash-light) 0%, var(--wash-mid) 55%, transparent 80%);
    filter: blur(10px);
    opacity: 0.95;
  }

  .cover__title-line {
    position: absolute; left: 0; right: 0;
    text-align: center;
    color: var(--title-blue);
    font-family: "Source Sans 3", sans-serif;
    font-weight: 400;
    line-height: 1;
  }
  .cover__title-line--top { top: 262px; font-size: 116px; letter-spacing: 8px; }
  .cover__title-line--bottom { top: 578px; font-size: 102px; letter-spacing: 4px; }

  .cover__title-accent {
    position: absolute; left: 0; right: 0; top: 372px;
    text-align: center;
    font-family: "Dancing Script", cursive;
    font-weight: 700;
    font-size: 190px;
    line-height: 1;
    color: var(--script-blue);
  }

  .cover__swoosh { position: absolute; left: 0; top: 0; width: 768px; height: 1086px; }

  .cover__subtitle {
    position: absolute; left: 0; right: 0; top: 790px;
    text-align: center;
    font-family: "Yellowtail", cursive;
    font-size: 58px;
    line-height: 80px;
    color: var(--script-blue);
    transform: rotate(-3deg);
  }
</style>
</head>
<body>
  <main class="cover">
    <p class="cover__author">DR. MERLE KUHNAST</p>

    <div class="cover__wash" role="img" aria-label="Aquarellfläche in Türkis- und Hellblautönen mit feinen goldenen Adern"></div>

    <h1 class="cover__title">
      <span class="cover__title-line cover__title-line--top">MORGENS</span>
      <span class="cover__title-accent">leise</span>
      <span class="cover__title-line cover__title-line--bottom">AUFBRECHEN</span>
    </h1>

    <svg class="cover__swoosh" viewBox="0 0 768 1086" aria-hidden="true">
      <path d="M0 893 C 90 880, 170 890, 258 944" fill="none" stroke="var(--swoosh)" stroke-width="4" stroke-linecap="round"/>
      <path d="M542 936 C 620 880, 690 832, 768 826" fill="none" stroke="var(--swoosh)" stroke-width="4" stroke-linecap="round"/>
    </svg>

    <p class="cover__subtitle">Geh den Pfad,<br>der dich leise ruft</p>
  </main>
</body>
</html>
```